HIGH-END ANTI AGING START-UP NEEDS DOCUMENT/LETTERHEAD DESIGN!!!!

We are a high end anti-aging and health start-up catering to clients in Stamford and NYC. We just did a logo redesign and are now looking for a letter head design that we can use IN GOOGLE DOCS for marwickcaregroup.example clients. We are REALLY EXCITED to see what you can show us!!!!!!!! We need something sophisticated and MODERN! Thanks so much!

Target Market(s)

High end, boutique medical clients. Our clientele is fairly high profile and we need a sleek, sophisticated letter head to put on all of our marketing materials and medical forms as well.

Industry/Entity Type

Medical

Font styles to use
Serif
Sans Serif

Colors
0255a3
ffffff
00a990
1b1b1b
919191

Requirements
Must have
• Must have the logo and "Marwick Care Group" written somewhere. Must have our URL www.marwickcaregroup.example.
Nice to have
• office phone number (203) 555-0147
Should not have
• Colors outside of our logo colors + grey + black

```html
<!DOCTYPE html>
<html lang="en">
<head>
<meta charset="utf-8">
<title>Marwick Care Group Letterhead</title>
<link rel="stylesheet" href="https://fonts.googleapis.com/css2?family=Arimo:wght@400&family=Montserrat:wght@400;600&family=Herr+Von+Muellerhoff&display=swap">
<style>
  :root {
    --backdrop: #e4e4e4;
    --paper: #ffffff;
    --brand-blue: #477de6;
    --brand-green: #0a9444;
    --ink: #1b1b1b;
    --muted: #919191;
  }
  * { box-sizing: border-box; margin: 0; padding: 0; }
  html, body {
    width: 1200px;
    height: 1200px;
    overflow: hidden;
    background: var(--backdrop);
  }
  .letterhead {
    position: absolute;
    left: 152px;
    top: 20px;
    width: 896px;
    height: 1160px;
    background: var(--paper);
    overflow: hidden;
  }
  .brand {
    position: absolute;
    left: 71px;
    top: 78px;
    display: flex;
    align-items: center;
    gap: 14px;
  }
  .brand-dot {
    width: 40px;
    height: 40px;
    border-radius: 50%;
    background: var(--brand-green);
  }
  .brand-name {
    font-family: "Montserrat", sans-serif;
    font-weight: 600;
    font-size: 24px;
    letter-spacing: 0.5px;
    color: var(--brand-blue);
  }
  .contact {
    position: absolute;
    right: 65px;
    top: 109px;
    font-family: "Montserrat", sans-serif;
    font-size: 19px;
    color: var(--ink);
  }
  .contact-label { color: var(--muted); }
  .letter-body {
    position: absolute;
    left: 115px;
    top: 318px;
    width: 670px;
    font-family: "Arimo", sans-serif;
    font-size: 15.6px;
    line-height: 20.5px;
    color: var(--ink);
  }
  .letter-body p + p { margin-top: 20.5px; }
  .sign-off {
    position: absolute;
    right: 120px;
    top: 705px;
    text-align: right;
  }
  .signature {
    font-family: "Herr Von Muellerhoff", cursive;
    font-size: 44px;
    line-height: 48px;
    color: var(--ink);
  }
  .signer-title {
    font-family: "Montserrat", sans-serif;
    font-size: 15.5px;
    color: var(--ink);
    margin-top: 2px;
  }
  .footer-wave {
    position: absolute;
    left: 0;
    bottom: 0;
    width: 896px;
    height: 100px;
    display: block;
  }
  .footer-url {
    position: absolute;
    left: 0;
    right: 0;
    top: 1088px;
    text-align: center;
    font-family: "Montserrat", sans-serif;
    font-size: 19px;
    letter-spacing: 0.3px;
    color: var(--ink);
  }
</style>
</head>
<body>
  <main class="letterhead">
    <header>
      <div class="brand">
        <span class="brand-dot"></span>
        <span class="brand-name">MARWICK CARE GROUP</span>
      </div>
      <div class="contact"><span class="contact-label">Phone:</span> (203) 555-0147</div>
    </header>

    <section class="letter-body">
      <p>Lorem ipsum dolor sit amet, consectetur adipiscing elit. Donec orci purus,<br>luctus vitae dignissim eu, iaculis sed purus. Vivamus faucibus, ipsum nec aliquet viverra, leo mauris condimentum ligula, sit amet sagittis enim ligula quis arcu. Nam egestas tortor id nisi porttitor mattis. In tortor ante, ultricies in suscipit a, tempus non massa. Vivamus et auctor mi. Fusce vel massa nulla. Phasellus nec eros mauris, et scelerisque orci. Donec malesuada orci vitae nulla accumsan porta a id massa. Quisque accumsan iaculis magna sit amet fringilla. Maecenas consequat, magna eget tincidunt semper, odio nibh rutrum mi, id feugiat ante nisi eu risus. Vestibulum nunc orci, rhoncus a placerat in, ultricies in mi. Cras mattis varius eros, vel fringilla nisi suscipit eget.</p>
      <p>Quisque scelerisque sagittis nulla at porttitor. Mauris a justo et tellus interdum tristique. Sed id augue vitae urna euismod commodo aliquet a quam. Pellentesque arcu velit, cursus et malesuada ut, consequat et diam. Nullam erat sem, rhoncus id ullamcorper vitae, rhoncus et arcu. In ultricies ultricies nulla, ut rutrum nisi iaculis at. Donec eu magna a metus ornare faucibus. Fusce aliquet faucibus ultricies. Morbi semper, est id tincidunt gravida, sem arcu adipiscing lacus, ac bibendum nulla leo eu purus. Quisque nec diam sed risus consectetur a ccumsan quis quis nibh. Vestibulum id purus lorem.</p>
    </section>

    <div class="sign-off">
      <div class="signature">Dana Ellery</div>
      <div class="signer-title">Program Director</div>
    </div>

    <footer>
      <div class="footer-url">www.marwickcaregroup.example</div>
      <svg class="footer-wave" viewBox="0 0 896 100" preserveAspectRatio="none" aria-hidden="true">
        <path d="M0 61 C 250 88, 560 98, 896 33 L 896 100 L 0 100 Z" fill="var(--brand-blue)"/>
        <path d="M0 33 C 250 72, 520 88, 896 26 C 540 84, 250 84, 0 53 Z" fill="var(--brand-green)"/>
      </svg>
    </footer>
  </main>
</body>
</html>
```